Kem7Dex Letterhead

Need a new letterhead for my law firm.
IDENTIFYING INFORMATION BELOW:
Ansel T Brightwater III
Attorney at Law
Address: 4832 Tillbury Rd, Ste 250, Dallas, TX 75204
Phone: 866-402-7183
Fax: 469-583-0271
Email: kem@kem7dex.example
Website: www.kem7dex.example

Colors
0054AA
0677BA
7BADD7
CADEEF
E8F1F8

Requirements
Must have
• Logo needs to be on the letterhead, along with identifying information which is included in the project description.

```html
<!DOCTYPE html>
<html lang="en">
<head>
<meta charset="utf-8">
<title>Kem7Dex Letterhead</title>
<link rel="stylesheet" href="https://fonts.googleapis.com/css2?family=Montserrat:wght@600;700&family=Questrial&display=swap">
<style>
  :root {
    --brand-deep: #0054AA;
    --brand-mid: #0677BA;
    --brand-light: #7BADD7;
    --brand-pale: #CADEEF;
    --brand-mist: #E8F1F8;
    --ink: #1b1b1b;
    --ink-soft: #333;
    --rule: #555;
    --paper: #ffffff;
    --backdrop: #ffffff;
  }
  * { box-sizing: border-box; margin: 0; padding: 0; }
  html, body { width: 1200px; height: 2804px; overflow: hidden; background: var(--backdrop); }
  .canvas { position: relative; width: 1200px; height: 2804px; }
  .letterhead {
    position: absolute; left: 233px; top: 1532px; width: 744px; height: 1053px;
    background: var(--paper);
    box-shadow: 0 6px 28px rgba(0,0,0,0.22);
    font-family: "Questrial", sans-serif; color: var(--ink);
    overflow: hidden;
  }
  .letterhead__bands { position: absolute; inset: 0; width: 744px; height: 1053px; }
  .brand-name {
    position: absolute; left: 62px; top: 30px;
    font-family: "Montserrat", sans-serif; font-weight: 700;
    font-size: 36px; letter-spacing: 2px; color: #fff;
  }
  .salutation { position: absolute; left: 58px; top: 162px; font-size: 19px; }
  .letter-body { position: absolute; left: 54px; top: 200px; width: 632px; }
  .letter-body p {
    font-size: 12.2px; line-height: 15px; text-align: justify; color: var(--ink-soft);
    margin-bottom: 15px;
  }
  .signature { position: absolute; left: 53px; top: 752px; }
  .signature__line { width: 276px; border-top: 2px dashed var(--ink-soft); margin: 0 0 20px 9px; }
  .person-name { font-family: "Montserrat", sans-serif; font-weight: 700; font-size: 19px; line-height: 24px; }
  .person-title { font-size: 18px; line-height: 26px; }
  .footer-rule { position: absolute; left: 44px; top: 917px; width: 645px; border-top: 1px solid var(--rule); }
  .footer-person { position: absolute; left: 53px; top: 940px; }
  .contact-list { position: absolute; list-style: none; font-size: 13px; }
  .contact-list li { display: flex; align-items: center; height: 18.5px; gap: 9px; }
  .contact-list svg { width: 13px; height: 13px; fill: var(--brand-deep); flex: none; }
  .contact-list--phone { left: 308px; top: 950px; font-family: "Montserrat", sans-serif; font-weight: 600; }
  .contact-list--phone li:last-child { font-family: "Questrial", sans-serif; font-weight: 400; }
  .contact-list--web { left: 476px; top: 946px; }
  .contact-list--web li.address { align-items: flex-start; height: auto; line-height: 18.5px; }
  .contact-list--web li.address svg { margin-top: 3px; }
</style>
</head>
<body>
<div class="canvas">
  <article class="letterhead">
    <svg class="letterhead__bands" viewBox="0 0 744 1053" aria-hidden="true">
      <defs>
        <linearGradient id="headGrad" x1="0" y1="0" x2="1" y2="0">
          <stop offset="0" stop-color="#0677BA"/>
          <stop offset="0.55" stop-color="#0a8fd2"/>
          <stop offset="1" stop-color="#0054AA"/>
        </linearGradient>
        <linearGradient id="footGrad" x1="0" y1="0" x2="1" y2="0">
          <stop offset="0" stop-color="#0054AA"/>
          <stop offset="0.7" stop-color="#0054AA"/>
          <stop offset="1" stop-color="#0a98da"/>
        </linearGradient>
      </defs>
      <path d="M0 0 H744 V14 H368 C338 14 330 20 320 42 L308 68 C299 86 290 94 266 94 H0 Z" fill="url(#headGrad)"/>
      <path d="M0 1041 H520 C534 1041 538 1025 562 1025 H744 V1053 H0 Z" fill="url(#footGrad)"/>
    </svg>

    <div class="brand-name">Kem7Dex</div>

    <p class="salutation">Dear Sir,</p>

    <div class="letter-body">
      <p>Quis ipsum suspendisse ultrices gravida. Risus commodo viverra maecenas accumsan lacus vel facilisis. Lorem ipsum dolor sit amet, consectetur adipiscing elit, sed do eiusmod tempor incididunt ut labore et dolore magna aliqua. Quis ipsum suspendisse ultrices gravida. Risus commodo viverra maecenas accumsan lacus vel facilisis. Lorem ipsum dolor sit amet, consectetur adipiscing elit, sed do eiusmod tempor incididunt ut labore et dolore magna aliqua. Quis ipsum suspendisse ultrices gravida. Risus commodo viverra maecenas accumsan lacus vel facilisis. Lorem ipsum dolor sit amet, consectetur adipiscing elit, sed do eiusmod tempor incididunt ut labore et dolore magna aliqua. Quis ipsum suspendisse ultrices gravida. Risus commodo viverra maecenas accumsan lacus vel facilisis.</p>
      <p>Lorem ipsum dolor sit amet, consectetur adipiscing elit, sed do eiusmod tempor incididunt ut labore et dolore magna aliqua. Quis ipsum suspendisse ultrices gravida. Risus commodo viverra maecenas accumsan lacus vel facilisis. Lorem ipsum dolor sit amet, consectetur adipiscing elit, sed do eiusmod tempor incididunt ut labore et dolore magna aliqua. Quis ipsum suspendisse ultrices gravida. Risus commodo viverra maecenas accumsan lacus vel facilisis. Lorem ipsum dolor sit amet, consectetur adipiscing elit, sed do eiusmod tempor incididunt ut labore et dolore magna aliqua. Quis ipsum suspendisse ultrices gravida. Risus commodo viverra maecenas accumsan lacus vel facilisis. Lorem ipsum dolor sit amet, consectetur adipiscing elit, sed do eiusmod tempor incididunt ut labore et dolore magna aliqua. Quis ipsum suspendisse ultrices gravida. Risus commodo viverra maecenas accumsan lacus vel facilisis.</p>
      <p>Lorem ipsum dolor sit amet, consectetur adipiscing elit, sed do eiusmod tempor incididunt ut labore et dolore magna aliqua. Quis ipsum suspendisse ultrices gravida. Risus commodo viverra maecenas accumsan lacus vel facilisis. Lorem ipsum dolor sit amet, consectetur adipiscing elit, sed do eiusmod tempor incididunt ut labore et dolore magna aliqua. Quis ipsum suspendisse ultrices gravida. Risus commodo viverra maecenas accumsan lacus vel facilisis. Lorem ipsum dolor sit amet, consectetur adipiscing elit, sed do eiusmod tempor incididunt ut labore et dolore magna aliqua. Quis ipsum suspendisse ultrices gravida. Risus commodo viverra maecenas accumsan lacus vel facilisis. Lorem ipsum dolor sit amet, consectetur adipiscing elit, sed do eiusmod tempor incididunt ut labore et dolore magna aliqua. Quis ipsum suspendisse ultrices gravida. Risus commodo viverra maecenas accumsan lacus vel facilisis. Lorem ipsum dolor sit amet, consectetur adipiscing elit, sed do eiusmod tempor incididunt ut labore et dolore magna aliqua. Quis ipsum suspendisse ultrices gravida. Risus commodo viverra maecenas accumsan lacus vel facilisis. Lorem ipsum dolor sit amet, consectetur adipiscing elit, sed do eiusmod tempor incididunt ut labore et dolore magna aliqua. Quis ipsum suspendisse ultrices gravida. Risus commodo viverra maecenas accumsan lacus vel facilisis.</p>
    </div>

    <div class="signature">
      <div class="signature__line"></div>
      <p class="person-name">Ansel T Brightwater III</p>
      <p class="person-title">Attorney at Law</p>
    </div>

    <div class="footer-rule"></div>

    <div class="footer-person">
      <p class="person-name">Ansel T Brightwater III</p>
      <p class="person-title">Attorney at Law</p>
    </div>

    <ul class="contact-list contact-list--phone">
      <li><svg viewBox="0 0 16 16"><path d="M3.5 1 L6 1.6 L6.6 4.8 L5 6 C5.8 8 7.9 10.2 10 11 L11.2 9.4 L14.4 10 L15 12.5 C15 14 13.8 15 12.4 15 C6.6 14.6 1.4 9.4 1 3.6 C1 2.2 2 1 3.5 1 Z"/></svg>866-402-7183</li>
      <li><svg viewBox="0 0 16 16"><path d="M4 1 H12 V5 H4 Z M1 6 H15 V12 H12.5 V15 H3.5 V12 H1 Z M5 10 V13.5 H11 V10 Z"/></svg>469-583-0271</li>
      <li><svg viewBox="0 0 16 16"><path d="M1 4 H15 V13 H1 Z M2.5 5.5 L8 9.5 L13.5 5.5 V5 H2.5 Z" fill-rule="evenodd"/></svg>kem@kem7dex.example</li>
    </ul>

    <ul class="contact-list contact-list--web">
      <li><svg viewBox="0 0 16 16"><path d="M8 1 A7 7 0 1 0 8.01 1 Z M2.6 7.2 H5.2 C5.3 5.3 5.8 3.7 6.6 2.6 A5.6 5.6 0 0 0 2.6 7.2 Z M6.6 7.2 H9.4 C9.3 5.2 8.7 3.5 8 2.5 C7.3 3.5 6.7 5.2 6.6 7.2 Z M10.8 7.2 H13.4 A5.6 5.6 0 0 0 9.4 2.6 C10.2 3.7 10.7 5.3 10.8 7.2 Z M2.6 8.8 A5.6 5.6 0 0 0 6.6 13.4 C5.8 12.3 5.3 10.7 5.2 8.8 Z M6.6 8.8 C6.7 10.8 7.3 12.5 8 13.5 C8.7 12.5 9.3 10.8 9.4 8.8 Z M10.8 8.8 C10.7 10.7 10.2 12.3 9.4 13.4 A5.6 5.6 0 0 0 13.4 8.8 Z" fill-rule="evenodd"/></svg>www.kem7dex.example</li>
      <li class="address"><svg viewBox="0 0 16 16"><path d="M8 1 C5.2 1 3.5 3 3.5 5.4 C3.5 8.4 8 12 8 12 C8 12 12.5 8.4 12.5 5.4 C12.5 3 10.8 1 8 1 Z M8 3.6 A1.8 1.8 0 1 0 8.01 3.6 Z M2 13 H14 V15 H2 Z" fill-rule="evenodd"/></svg><span>4832 Tillbury Rd, Ste<br>250, Dallas, TX 75204</span></li>
    </ul>
  </article>
</div>
</body>
</html>
```